business cards foreign exchange student company
Bluebird Hosting
Bright & Fun-filled
Mack Dorran
Service Director
Western Region
mack@mybluebirdhosting.com
mybluebirdhosting.com
This business card needs to be unforgettable! It needs to stand out from all the other business cards. Something clever/funny. It needs to communicate this is fun!! this is exciting!! and our theme for our company is "The Best Time Ever!" so the business card should convey that they have just found The Best Time Ever!!!
This will be my new website (with the old logo)
this is a marketing piece used to send families to the website
another marketing piece to get families to the website
This is my logo .ai file
This is my .ai logo file for dark backgrounds

```html
<!DOCTYPE html>
<html lang="en">
<head>
<meta charset="utf-8">
<title>Bluebird Hosting – Business Card Options</title>
<link rel="stylesheet" href="https://fonts.googleapis.com/css2?family=Arimo:wght@400;700&family=Tinos:ital,wght@1,700&display=swap">
<style>
  :root {
    --stage: #5b5b5b;
    --caption: #e4e4e4;
    --white: #ffffff;
    --green-light: #8fd13a;
    --green-dark: #2f8a12;
    --blue-light: #2d7fd0;
    --blue-dark: #0a2a63;
    --navy: #0d3270;
    --navy-deep: #081f4a;
    --ink: #1f2a3a;
    --ink-soft: #4d5868;
    --brand-blue: #13408c;
  }
  * { margin: 0; padding: 0; box-sizing: border-box; }
  html, body { width: 1200px; height: 847px; overflow: hidden; }
  body {
    background: var(--stage);
    font-family: "Arimo", Arial, sans-serif;
    position: relative;
  }
  .card-option { position: absolute; top: 211px; width: 144px; }
  .card-option--1 { left: 235px; }
  .card-option--2 { left: 521px; }
  .card-option--3 { left: 802px; }
  .card {
    position: relative;
    width: 144px; height: 259px;
    border-radius: 6px;
    overflow: hidden;
    color: var(--white);
    box-shadow: 0 3px 8px rgba(0,0,0,.45);
  }
  .card--green { background: linear-gradient(160deg, var(--green-light) 20%, var(--green-dark) 100%); }
  .card--blue  { background: linear-gradient(160deg, var(--blue-light) 15%, var(--blue-dark) 95%); }
  .card--white { background: var(--white); color: var(--ink); }
  .card__shape { position: absolute; inset: 0; width: 100%; height: 100%; }
  .brand {
    position: absolute; top: 14px; left: 0; right: 0;
    text-align: center;
    font-weight: 700; font-size: 11px;
    color: var(--brand-blue);
    letter-spacing: -0.2px;
  }
  .card--white .brand { color: var(--white); top: 11px; }
  .brand__dot {
    display: inline-block; width: 6px; height: 6px;
    border-radius: 50%; background: currentColor;
    margin-right: 3px; vertical-align: 1px;
  }
  .faint-mark {
    position: absolute; left: 32px; top: 92px;
    width: 80px; height: 80px; border-radius: 50%;
    border: 7px solid rgba(255,255,255,.14);
  }
  .card--white .faint-mark { border-color: rgba(13,50,112,.08); }
  .person { position: absolute; top: 60px; left: 0; right: 0; text-align: center; }
  .person__name { font-weight: 700; font-size: 11.5px; letter-spacing: .3px; }
  .person__role { font-size: 5.5px; margin-top: 2px; opacity: .9; }
  .person__email { font-size: 5.5px; margin-top: 2px; }
  .contact {
    position: absolute; top: 140px; left: 30px;
    font-size: 5px; line-height: 7px;
  }
  .tagline {
    position: absolute; top: 206px; left: 0; right: 0; text-align: center;
    font-family: "Tinos", "Times New Roman", serif;
    font-style: italic; font-weight: 700; font-size: 10px;
  }
  .card--white .tagline { color: var(--white); top: 214px; }
  .website {
    position: absolute; bottom: 9px; left: 0; right: 0; text-align: center;
    font-size: 4.5px; letter-spacing: .3px; opacity: .85;
  }
  .card--white .website { color: var(--white); bottom: 7px; }
  .caption {
    margin-top: 12px; text-align: center;
    font-size: 9px; color: var(--caption);
  }
</style>
</head>
<body>

  <section class="card-option card-option--1">
    <div class="card card--green">
      <svg class="card__shape" viewBox="0 0 144 259" preserveAspectRatio="none" aria-hidden="true">
        <path d="M0 0H144V46C100 40 50 54 0 48Z" fill="#ffffff"/>
      </svg>
      <div class="brand"><span class="brand__dot"></span>Bluebird Hosting</div>
      <div class="faint-mark"></div>
      <div class="person">
        <div class="person__name">Mack Dorran</div>
        <div class="person__role">Service Director</div>
        <div class="person__email">mack@mybluebirdhosting.com</div>
      </div>
      <div class="contact">
        Mobile: 555 014 2287<br>Toll Free: 1 800 555 0199<br>Western Region
      </div>
      <div class="tagline">The Best Time Ever!</div>
      <div class="website">www.mybluebirdhosting.com</div>
    </div>
    <p class="caption">One Sided 1</p>
  </section>

  <section class="card-option card-option--2">
    <div class="card card--blue">
      <svg class="card__shape" viewBox="0 0 144 259" preserveAspectRatio="none" aria-hidden="true">
        <path d="M0 0H144V46C100 40 50 54 0 48Z" fill="#ffffff"/>
      </svg>
      <div class="brand"><span class="brand__dot"></span>Bluebird Hosting</div>
      <div class="faint-mark"></div>
      <div class="person">
        <div class="person__name">Mack Dorran</div>
        <div class="person__role">Service Director</div>
        <div class="person__email">mack@mybluebirdhosting.com</div>
      </div>
      <div class="contact">
        Mobile: 555 014 2287<br>Toll Free: 1 800 555 0199<br>Western Region
      </div>
      <div class="tagline">The Best Time Ever!</div>
      <div class="website">www.mybluebirdhosting.com</div>
    </div>
    <p class="caption">One Sided 2</p>
  </section>

  <section class="card-option card-option--3">
    <div class="card card--white">
      <svg class="card__shape" viewBox="0 0 144 259" preserveAspectRatio="none" aria-hidden="true">
        <defs>
          <linearGradient id="bandTop" x1="0" y1="0" x2="0" y2="1">
            <stop offset="0" stop-color="#0d3270"/>
            <stop offset="1" stop-color="#1d5cab"/>
          </linearGradient>
          <linearGradient id="bandBottom" x1="0" y1="0" x2="1" y2="1">
            <stop offset="0" stop-color="#1d5cab"/>
            <stop offset="1" stop-color="#081f4a"/>
          </linearGradient>
        </defs>
        <path d="M0 0H144V34C100 44 50 28 0 38Z" fill="url(#bandTop)"/>
        <path d="M0 208C50 196 100 214 144 196V259H0Z" fill="#8fb6e4" opacity=".5"/>
        <path d="M0 214C50 202 100 220 144 204V259H0Z" fill="url(#bandBottom)"/>
      </svg>
      <div class="brand"><span class="brand__dot"></span>Bluebird Hosting</div>
      <div class="faint-mark"></div>
      <div class="person">
        <div class="person__name">Mack Dorran</div>
        <div class="person__role">Service Director</div>
        <div class="person__email">mack@mybluebirdhosting.com</div>
      </div>
      <div class="contact">
        Mobile: 555 014 2287<br>Toll Free: 1 800 555 0199<br>Western Region
      </div>
      <div class="tagline">The Best Time Ever!</div>
      <div class="website">www.mybluebirdhosting.com</div>
    </div>
    <p class="caption">One Sided 3</p>
  </section>

</body>
</html>
```